Business Card Design Project - IT Company

CLOUD IT company working with medium to large corporate clients requires 2 sided Business Card design.

Strong, Professional and modern is what I am looking for.

The Logo JPG attached has all the colour palette options. which consist of Red and Silver on various backgrounds

Preferred option for the Back of card is either Silver Text on Red or Silver Text on Black. Though this is not concrete. Surprise me.

Logo must be prominent along with Contact details of the staff member

Tagline can be all Capitals " CLOUD MANAGED SERVICES"

I will look to provide feedback and tweaks to get the right design so it should be a fun process.

I will provide the layered files to the top few contenders.

Reason: Leaving the door open for some creativity. Don't forget this is an technology company. .

Target Market(s)

Leaders, decision makers, CEOs, CIOs,

Industry/Entity Type

Business

Requirements
Must have
• Data must have is

Company Name: Brelquist
Tagline: Cloud Managed Services

No Particular order

First Name Last name
Director
Mobile 0477 555 019
www.brelquist-example.com
First.Lastname@brelquist-example.com
Suite 7, 48 Wexmoor Lane, Sydney NSW 2000

```html
<!DOCTYPE html>
<html lang="en">
<head>
<meta charset="utf-8">
<title>Brelquist Business Card</title>
<link rel="stylesheet" href="https://fonts.googleapis.com/css2?family=Arimo:wght@400;700&display=swap">
<style>
  :root {
    --page-bg: #e8e5e1;
    --card-bg: #000000;
    --silver: #d2d2d2;
    --silver-light: #e6e6e6;
    --brand-red: #a1262b;
    --white: #ffffff;
  }
  * { box-sizing: border-box; margin: 0; padding: 0; }
  html, body {
    width: 1200px;
    height: 1000px;
    overflow: hidden;
    background: var(--page-bg);
    font-family: "Arimo", Arial, sans-serif;
  }
  .canvas {
    position: relative;
    width: 1200px;
    height: 1000px;
  }
  .card {
    position: absolute;
    left: 304px;
    width: 592px;
    height: 320px;
    background: var(--card-bg);
    border-radius: 18px;
    overflow: hidden;
    color: var(--silver);
  }
  .card--front { top: 178px; }
  .card--back { top: 516px; }

  .brand {
    position: absolute;
    display: flex;
    flex-direction: column;
    align-items: flex-end;
  }
  .brand__row {
    display: flex;
    align-items: center;
  }
  .brand__dot {
    border-radius: 50%;
    background: var(--silver);
  }
  .brand__name {
    font-weight: 700;
    color: var(--silver);
    line-height: 1;
  }
  .brand__tagline {
    font-weight: 700;
    color: var(--silver);
    letter-spacing: 0.02em;
    line-height: 1;
  }

  .card--front .brand { left: 40px; top: 112px; width: 500px; }
  .card--front .brand__dot { width: 62px; height: 62px; margin-right: 26px; }
  .card--front .brand__name { font-size: 82px; letter-spacing: -1px; }
  .card--front .brand__tagline { font-size: 19px; margin-top: 8px; margin-right: 10px; }

  .card--back .brand { left: 272px; top: 224px; width: 272px; }
  .card--back .brand__dot { width: 34px; height: 34px; margin-right: 14px; }
  .card--back .brand__name { font-size: 46px; letter-spacing: -0.5px; }
  .card--back .brand__tagline { font-size: 11px; margin-top: 3px; margin-right: 6px; }

  .person {
    position: absolute;
    top: 48px;
    left: 0;
    width: 100%;
    text-align: center;
  }
  .person__name {
    font-size: 37px;
    font-weight: 700;
    color: var(--silver-light);
    line-height: 1;
  }
  .person__role {
    display: flex;
    justify-content: center;
    align-items: center;
    gap: 8px;
    margin-top: 14px;
    font-size: 18px;
    font-weight: 700;
    color: var(--silver-light);
  }
  .person__role-dot {
    width: 20px;
    height: 20px;
    border-radius: 50%;
    border: 2px solid var(--silver);
  }
  .person__address {
    margin-top: 18px;
    font-size: 12.5px;
    font-weight: 700;
    color: var(--silver-light);
  }

  .contact-tab {
    position: absolute;
    left: 0;
    top: 210px;
    width: 36px;
    height: 78px;
    background: var(--brand-red);
    border-radius: 0 4px 4px 0;
    display: flex;
    flex-direction: column;
    justify-content: space-around;
    align-items: center;
    padding: 4px 0;
  }
  .contact-tab svg { width: 16px; height: 16px; }

  .contact-list {
    position: absolute;
    left: 55px;
    top: 213px;
    list-style: none;
    font-size: 12.5px;
    font-weight: 700;
    color: var(--silver-light);
  }
  .contact-list li { height: 25px; line-height: 16px; }
</style>
</head>
<body>
<main class="canvas">
  <section class="card card--front" aria-label="Card front">
    <div class="brand">
      <div class="brand__row">
        <span class="brand__dot"></span>
        <span class="brand__name">Brelquist</span>
      </div>
      <span class="brand__tagline">CLOUD MANAGED SERVICES</span>
    </div>
  </section>

  <section class="card card--back" aria-label="Card back">
    <div class="person">
      <h1 class="person__name">First Name Last name</h1>
      <p class="person__role"><span class="person__role-dot"></span>DIRECTOR</p>
      <p class="person__address">Suite 7, 48 Wexmoor Lane, Sydney NSW 2000</p>
    </div>

    <div class="contact-tab">
      <svg viewBox="0 0 16 16" fill="none" stroke="#ffffff" stroke-width="1.3" aria-label="Email">
        <rect x="1.5" y="3.5" width="13" height="9" rx="1"/>
        <path d="M1.5 4l6.5 5 6.5-5"/>
      </svg>
      <svg viewBox="0 0 16 16" fill="none" stroke="#ffffff" stroke-width="1.2" aria-label="Website">
        <circle cx="8" cy="8" r="6.5"/>
        <ellipse cx="8" cy="8" rx="3" ry="6.5"/>
        <path d="M1.5 8h13M2.5 4.8h11M2.5 11.2h11"/>
      </svg>
      <svg viewBox="0 0 16 16" fill="none" stroke="#ffffff" stroke-width="1.3" aria-label="Phone">
        <path d="M3 1.8l2.6 0.2 1 3.2-1.6 1.3a8 8 0 0 0 4.5 4.5l1.3-1.6 3.2 1 .2 2.6c-.3.8-1.3 1.3-2.3 1.2C6.8 13.8 2.2 9.2 1.8 4.1 1.7 3.1 2.2 2.1 3 1.8z"/>
      </svg>
    </div>

    <ul class="contact-list">
      <li>First.Lastname@brelquist-example.com</li>
      <li>www.brelquist-example.com</li>
      <li>0477 555 019</li>
    </ul>

    <div class="brand">
      <div class="brand__row">
        <span class="brand__dot"></span>
        <span class="brand__name">Brelquist</span>
      </div>
      <span class="brand__tagline">CLOUD MANAGED SERVICES</span>
    </div>
  </section>
</main>
</body>
</html>
```